Business Card Design Project (Beer industry)

I am seeking a redesign of my business card. I am looking for something that will really stand out in both texture and feel. Something more on the modern side then traditional. Nothing die cut shaped like a beer mug please.

The card is used mostly for other industry professionals, as well as bar and restaurant owners. My title is Strategy & Acquisitions. If you would like to somehow incorporate that theme, that may work.

My business is craft and imported beer. Nothing fizzy and yellow, so my products are more on the upscale side.
Updates

I was able to update my logo in .ai and .tif format. I hope that helps. 

Thank you all for your creative ideas. I have uploaded my current business card in pdf format, as well as our logo in .eps file format. We are excited about the submissions so far and want to thank you all again.

PS Please do not include fax number in future submissions, as we are looking for something more creative and a fax says 1999 and not 2015, which is the message we are going for, without being futuristic. 

Thank you all once again for all of your submissions. If we would consider a two sided card, we would like the opposite side not to be the same as the front. The styles we have seen so far, it appears the front and back are too similar. Again, a two sided card is not required. Thank you and we look forward to pushing the boundaries of your creativity. Cheers

Target Market(s)

My card would mostly go to bar and restaurant operators as well as other beer industry professionals

Industry/Entity Type

Restaurant

Requirements
Nice to have
• Two sided would be considered, although not required
Should not have
• Anything die cut shaped like a beer mug.

```html
<!DOCTYPE html>
<html lang="en">
<head>
<meta charset="utf-8">
<title>Harborline Beer – Business Card</title>
<link href="https://fonts.googleapis.com/css2?family=Exo+2:wght@400;500;600&display=swap" rel="stylesheet">
<style>
  :root {
    --backdrop: #2a2a2a;
    --card: #ffffff;
    --wine: #7d1418;
    --wine-bright: #b31f25;
    --ink: #3a3a3a;
    --paper-soft: #f3e6e6;
  }
  * { box-sizing: border-box; margin: 0; padding: 0; }
  html, body {
    width: 1200px; height: 1194px; overflow: hidden;
    background: var(--backdrop);
    font-family: "Exo 2", Arial, sans-serif;
  }
  .card {
    position: absolute; left: 232px; width: 736px; height: 420px;
    background: var(--card);
    box-shadow: 0 6px 18px rgba(0,0,0,.45);
    overflow: hidden;
  }
  .card--front { top: 101px; }
  .card--back {
    top: 644px;
    background: linear-gradient(135deg, var(--wine-bright), var(--wine));
  }

  .brand {
    position: absolute; display: flex; flex-direction: column; align-items: center;
    text-align: center; white-space: nowrap;
  }
  .brand__row { display: flex; align-items: center; gap: 10px; }
  .brand__dot { border-radius: 50%; background: var(--wine-bright); }
  .brand__name { color: var(--wine-bright); font-weight: 600; letter-spacing: 1px; }
  .brand__tagline { color: var(--ink); margin-top: 10px; }

  .card--front .brand { left: 20px; top: 190px; width: 360px; }
  .card--front .brand__dot { width: 18px; height: 18px; }
  .card--front .brand__name { font-size: 30px; }
  .card--front .brand__tagline { font-size: 14px; }

  .card--back .brand { left: 0; top: 165px; width: 736px; }
  .card--back .brand__dot { width: 24px; height: 24px; background: var(--card); }
  .card--back .brand__name { font-size: 48px; color: var(--card); }
  .card--back .brand__tagline { font-size: 18px; color: var(--paper-soft); margin-top: 14px; }

  .person { position: absolute; left: 432px; top: 62px; color: var(--ink); }
  .person__name { color: var(--wine); font-size: 35px; font-weight: 600; line-height: 1; white-space: nowrap; }
  .person__title { font-size: 21px; font-weight: 500; margin-top: 6px; }
  .contact { list-style: none; margin-top: 40px; font-size: 23px; line-height: 34px; white-space: nowrap; }

  .address-band {
    position: absolute; left: 0; bottom: 0; width: 100%; height: 54px;
    background: linear-gradient(90deg, var(--wine-bright), var(--wine));
    color: #fff; font-size: 20px; line-height: 54px; padding-left: 54px;
    white-space: nowrap;
  }
</style>
</head>
<body>
  <section class="card card--front">
    <div class="brand">
      <div class="brand__row">
        <span class="brand__dot"></span>
        <span class="brand__name">HARBORLINE BEER</span>
      </div>
      <p class="brand__tagline">Premier Craft &amp; Import Beer Distributor</p>
    </div>
    <div class="person">
      <h1 class="person__name">DANA KESSLER</h1>
      <p class="person__title">Strategy &amp; Acquisitions</p>
      <ul class="contact">
        <li>Cell: (555) 014-2287</li>
        <li>dana@harborlinebeer.com</li>
        <li>www.harborlinebeer.com</li>
      </ul>
    </div>
    <div class="address-band">48 Fenwick Street, Brooklyn, NY 11201 - Phone: (555) 018-7200</div>
  </section>

  <section class="card card--back">
    <div class="brand">
      <div class="brand__row">
        <span class="brand__dot"></span>
        <span class="brand__name">HARBORLINE BEER</span>
      </div>
      <p class="brand__tagline">Premier Craft &amp; Import Beer Distributor</p>
    </div>
  </section>
</body>
</html>
```